Website Design for my Copper Distillation Equipment Business Nature Sciencey Theme

I already have a website www.halvorkettleworks.com and its a pixelhut website builder one. But I cannot get the design right at all. I need this fixed.

I have logo. I need a redesign, for my website, the home page, that maybe I can have something similar in design- I can use as template to copy, for other pages so the whole thing matches? Look at my website so you understand I have a few pages...but most are links. Its a competition. Code has to be easy for me to implement, I am not expert.

Your advice needed..It would be a plus if I can update this myself throughout time. If I could have this explained to me too, the maintenance of it...how would I do this too..etc..pretend I am a child when you explain, if you can. I am not good with this stuff but I am smart and can learn fast.

I want a high end look. Maybe like an ivy league college-y look too, real preppy, chemistry...science-y, nature like is good, leaves, drops water, fields of wheat, lavender, etc.

I want every page to look similar, but the home page is what I want to be the main showpiece,..and I want each page have a little text section, maybe a photos section and a video section, for that market. Like a nice website. If I am not doing this right, let me know. I can work with you. Just help me, please. Let me know if I am doing this right.

When I pick my winning design, for my website, I will hire the artist one-on-one to re-design my shopping cart next. Or if I need additional help with implementing this current design, I can hire the same artist again too. I have a blog that I may want to hire the redesign as well too, but later on. My point is I am not just looking for one project here but I want to follow up with winning artist. So it would be return business for the winner.

I got my logo done here so I am repeat customer. And I have given that winning artist other design work.

Target Market(s)

Moonshine Stills I sell most, Essential Oil Business, Micro and Craft Distilleries, Canna-businesses, Alcohol Fuel

Industry/Entity Type

Business

Number of Pages Required

5+ page

Colors
ec1f27

Requirements
Must have
• The categories for the stills must be prominent and eye catching. The main photo I would like to be naturelike theme, but you can try out different things with me. I am open to ideas and suggestions. I would like this to be implemented easy and fast.
Nice to have
• My logo in it. You can use any of my photos as well from my snapvale account. https://www.snapvale.net/photos/81726354@X07/
• Colors of my Logo...matching design.
• Maybe some basic stock photos you see would match for me..
• Chemistry like symbols for the categories, I love that.

```html
<!DOCTYPE html>
<html lang="en">
<head>
<meta charset="utf-8">
<title>Halvor Kettleworks — Copper Distillation Equipment</title>
<link href="https://fonts.googleapis.com/css2?family=Open+Sans:wght@400;600;700&display=swap" rel="stylesheet">
<style>
  :root{
    --maroon:#5b1b1f;
    --maroon-deep:#3e1013;
    --maroon-panel:#6e2227;
    --maroon-dark:#4a1418;
    --button:#7a1f24;
    --accent:#ec1f27;
    --ink:#222;
    --ink-soft:#777;
    --paper:#ffffff;
    --mist:#efefef;
    --nav:#111;
  }
  *{box-sizing:border-box;margin:0;padding:0}
  html,body{width:1200px;height:2872px;overflow:hidden}
  body{
    position:relative;
    font-family:"Open Sans",Arial,sans-serif;
    color:var(--ink);
    background:
      radial-gradient(ellipse 700px 260px at 600px 0,#8a3036 0%,rgba(138,48,54,0) 100%),
      linear-gradient(180deg,var(--maroon) 0%,var(--maroon-deep) 100%);
  }
  .brand{position:absolute;top:44px;left:0;width:1200px;display:flex;flex-direction:column;align-items:center;gap:10px}
  .brand-mark{width:96px;height:96px;border-radius:50%;background:var(--paper)}
  .brand-name{font-weight:700;font-size:22px;color:var(--paper);letter-spacing:1px}

  .page{position:absolute;left:112px;top:228px;width:976px;height:2500px;background:var(--paper);
        border-radius:0 0 50% 50% / 0 0 60px 60px;overflow:hidden}

  .main-nav{height:40px;background:var(--nav);display:flex;align-items:center;padding-left:24px;gap:26px}
  .main-nav a{color:#fff;font-size:14px;font-weight:700;text-decoration:none}

  .hero{position:relative;height:504px;background:linear-gradient(135deg,#c9c9c9 0%,#7d7d7d 45%,#3a3a3a 100%)}
  .hero-caption{position:absolute;right:40px;bottom:70px;color:#fff;font-size:44px;font-weight:400}
  .hero-dots{position:absolute;right:40px;bottom:24px;display:flex;gap:8px}
  .hero-dots span{width:10px;height:10px;border-radius:50%;background:#fff;opacity:.6}
  .hero-dots span:first-child{opacity:1}

  .categories{display:flex;height:316px;background:var(--maroon-panel)}
  .categories-intro{width:280px;background:var(--maroon-dark);color:#fff;font-size:26px;font-weight:700;line-height:1.35;padding:60px 34px}
  .categories-list{flex:1;display:grid;grid-template-columns:244px 220px 200px;grid-auto-rows:72px;padding:38px 0 0 96px}
  .category{display:flex;align-items:center;gap:18px;color:#fff;font-size:17px;font-weight:700}
  .category svg{width:30px;height:30px;flex:none}

  .section-title{text-align:center;font-size:32px;font-weight:700;color:var(--ink);line-height:44px}
  .featured{padding-top:44px}
  .video{position:relative;margin:30px auto 0;width:576px;height:388px;border:4px solid #fff;box-shadow:0 2px 10px rgba(0,0,0,.35);
         background:linear-gradient(135deg,#6b2a20 0%,#b57a58 45%,#d8d2c8 100%)}
  .video-play{position:absolute;left:50%;top:44%;transform:translate(-50%,-50%)}
  .video-caption{position:absolute;left:0;right:0;bottom:0;height:52px;background:rgba(0,0,0,.75);color:#fff;font-size:15px;font-weight:600;padding:16px 20px}

  .purity{padding-top:60px}
  .feature-cards{display:flex;gap:20px;margin-top:28px}
  .card{width:312px}
  .card-photo{height:204px}
  .card h3{margin-top:20px;font-size:20px;line-height:28px;font-weight:700;color:var(--button)}
  .card .sub{font-size:14px;font-weight:600;margin-top:2px}
  .card p{margin-top:16px;font-size:12px;line-height:22px;color:var(--ink-soft);padding-right:20px}
  .btn{display:inline-block;margin-top:20px;background:var(--button);color:#fff;font-size:13px;font-weight:700;padding:9px 22px;border-radius:3px}

  .products{position:absolute;left:0;top:2010px;width:976px;height:490px;background:var(--mist);padding-top:60px}
  .product-row{display:flex;gap:28px;margin:36px 0 0 70px}
  .product{width:260px}
  .product-photo{height:200px}
  .product h3{margin-top:16px;font-size:17px;line-height:24px;font-weight:700;white-space:nowrap}
  .product .sub{font-size:13px;color:var(--ink-soft);margin-top:2px;height:36px}
  .product .btn{margin-top:12px}
  .arrow{position:absolute;top:250px;font-size:30px;color:#555}

  .footer{position:absolute;left:0;top:2736px;width:1200px;text-align:center;color:#fff}
  .social{display:flex;justify-content:center;gap:16px}
  .social span{width:34px;height:34px;border-radius:50%;background:#fff}
  .footer-nav{margin-top:18px;display:flex;justify-content:center;gap:14px;font-size:12px;font-weight:700}
  .footer-nav span.sep{opacity:.6}
  .copyright{margin-top:10px;font-size:11px;font-weight:600}
</style>
</head>
<body>
  <header class="brand">
    <div class="brand-mark"></div>
    <div class="brand-name">HALVOR KETTLEWORKS</div>
  </header>

  <main class="page">
    <nav class="main-nav">
      <a>HOME</a><a>ABOUT US</a><a>CONTACT US</a><a>PHOTO</a><a>VIDEO</a><a>SHOP</a><a>BLOG</a><a>BOOKS</a><a>LINKS</a>
    </nav>

    <section class="hero" role="img" aria-label="Black and white photo of a copper still with pipes and clamps">
      <div class="hero-caption">Halvor Kettleworks</div>
      <div class="hero-dots"><span></span><span></span><span></span></div>
    </section>

    <section class="categories">
      <div class="categories-intro">Please Choose the Category of the Still you are looking for</div>
      <div class="categories-list">
        <div class="category"><svg viewBox="0 0 30 30"><path d="M11 3h8M13 3v9L5 26h20L17 12V3" fill="none" stroke="#fff" stroke-width="2"/></svg>Stills</div>
        <div class="category"><svg viewBox="0 0 30 30"><rect x="7" y="8" width="16" height="18" rx="3" fill="#fff"/><rect x="12" y="3" width="6" height="5" fill="#fff"/></svg>Boilers</div>
        <div class="category"><svg viewBox="0 0 30 30"><path d="M4 26V12l11-8 11 8v14z" fill="#fff"/></svg>Distillery</div>
        <div class="category"><svg viewBox="0 0 30 30"><path d="M15 3C11 10 8 14 8 19a7 7 0 0 0 14 0c0-5-3-9-7-16z" fill="#fff"/></svg>Essential Oils</div>
        <div class="category"><svg viewBox="0 0 30 30"><path d="M3 15L15 4l12 11h-3v11H6V15z" fill="#fff"/></svg>Home Distillers</div>
        <div class="category"><svg viewBox="0 0 30 30"><rect x="5" y="9" width="20" height="16" fill="#fff"/><path d="M11 9V5h8v4" fill="none" stroke="#fff" stroke-width="2"/></svg>Kits</div>
        <div class="category"><svg viewBox="0 0 30 30"><rect x="8" y="6" width="14" height="20" rx="2" fill="#fff"/><rect x="11" y="2" width="8" height="4" fill="#fff"/></svg>Alcohol Fuel</div>
        <div class="category"><svg viewBox="0 0 30 30"><path d="M12 2h6v7l4 4v15H8V13l4-4z" fill="#fff"/></svg>Vodka Still</div>
        <div class="category"><svg viewBox="0 0 30 30"><circle cx="15" cy="15" r="8" fill="none" stroke="#fff" stroke-width="4"/><circle cx="15" cy="15" r="2" fill="#fff"/></svg>Parts</div>
        <div class="category"><svg viewBox="0 0 30 30"><path d="M15 3c-2 6-2 12 0 22c2-10 2-16 0-22zM4 10c4 4 7 8 11 15C10 21 6 16 4 10zM26 10c-4 4-7 8-11 15c5-4 9-9 11-15z" fill="#fff"/></svg>Cannabis</div>
        <div class="category"><svg viewBox="0 0 30 30"><path d="M15 2c3 6 9 9 9 16a9 9 0 0 1-18 0c0-4 2-6 4-8 0 3 1 5 3 5-1-5 0-9 2-13z" fill="#fff"/></svg>Heat Central</div>
      </div>
    </section>

    <section class="featured">
      <h2 class="section-title">Featured Video</h2>
      <div class="video" role="img" aria-label="Video still of hands fitting a copper clamp to a still column">
        <svg class="video-play" width="64" height="64" viewBox="0 0 64 64"><circle cx="32" cy="32" r="30" fill="rgba(0,0,0,.55)"/><path d="M26 20l18 12-18 12z" fill="#fff"/></svg>
        <div class="video-caption">Halvor Kettleworks Alchemist</div>
      </div>
    </section>

    <section class="purity">
      <h2 class="section-title">Purity comes from a direct connection with Nature...</h2>
      <div class="feature-cards">
        <article class="card">
          <div class="card-photo" role="img" aria-label="Copper stills standing outside a brick building" style="background:linear-gradient(135deg,#9a8f80,#b88860 55%,#6e6a5a)"></div>
          <h3>Home Distillers!</h3>
          <div class="sub">We sell Copper Stills.</div>
          <p>If you can fabricate, you can build this still with a small amount of copper pipe, a solid boiler and patience. Our commitment to fine craftsmanship can be seen in every detail.</p>
          <span class="btn">Read More</span>
        </article>
        <article class="card">
          <div class="card-photo" role="img" aria-label="Polished micro distillery column in a workshop" style="background:linear-gradient(135deg,#d9d9d9,#8c8c8c 50%,#5a5a5a)"></div>
          <h3>Micro Distillery Equipment</h3>
          <div class="sub">Copper Stills for Sale!</div>
          <p>If you can fabricate, you can build this still with a small amount of copper pipe, a solid boiler and patience. Our commitment to fine craftsmanship can be seen in every detail.</p>
          <span class="btn">Read More</span>
        </article>
        <article class="card">
          <div class="card-photo" role="img" aria-label="Herbal extractor among green plants" style="background:linear-gradient(135deg,#2f5a22,#b06a3a 50%,#1f3a18)"></div>
          <h3>Hearthfield Herbal Extractor</h3>
          <div class="sub">Make Cannabis Oil with Alcohol!</div>
          <p>If you can fabricate, you can build this still with a small amount of copper pipe, a solid boiler and patience. Our commitment to fine craftsmanship can be seen in every detail.</p>
          <span class="btn">Read More</span>
        </article>
      </div>
    </section>

    <section class="products">
      <h2 class="section-title">Our Products</h2>
      <span class="arrow" style="left:26px">‹</span>
      <span class="arrow" style="right:26px">›</span>
      <div class="product-row">
        <article class="product">
          <div class="product-photo" role="img" aria-label="30 gallon copper boiler on a lawn" style="background:linear-gradient(135deg,#6f8a4a,#b8a47e 50%,#7a6a50)"></div>
          <h3>30 Gallon Boiler</h3>
          <div class="sub">30 gallon boiler shown here with many possibilities.</div>
          <span class="btn">Buy A Still! Click Here</span>
        </article>
        <article class="product">
          <div class="product-photo" role="img" aria-label="Micro distillery equipment standing outdoors" style="background:linear-gradient(135deg,#5e7a3a,#c9c9c9 50%,#7a5a3a)"></div>
          <h3>Micro Distillery Equipment</h3>
          <div class="sub">Copper Stills for Sale!</div>
          <span class="btn">Buy A Still! Click Here</span>
        </article>
        <article class="product">
          <div class="product-photo" role="img" aria-label="Herbal extractor control box with copper fittings" style="background:linear-gradient(135deg,#cfcfcf,#a06a4a 50%,#6a3a2a)"></div>
          <h3>Hearthfield Herbal Extractor</h3>
          <div class="sub">Make Cannabis Oil with Alcohol!</div>
          <span class="btn">Buy A Still! Click Here</span>
        </article>
      </div>
    </section>
  </main>

  <footer class="footer">
    <div class="social" aria-label="Social links"><span></span><span></span></div>
    <div class="footer-nav">
      <span>HOME</span><span class="sep">|</span><span>ABOUT US</span><span class="sep">|</span><span>CONTACT US</span><span class="sep">|</span><span>PHOTO</span><span class="sep">|</span><span>VIDEO</span><span class="sep">|</span><span>SHOP</span><span class="sep">|</span><span>BLOG</span><span class="sep">|</span><span>BOOKS</span><span class="sep">|</span><span>LINKS</span>
    </div>
    <div class="copyright">© 2015 HALVOR KETTLEWORKS, ALL RIGHTS RESERVED</div>
  </footer>
</body>
</html>
```